Landing Page for Martial Arts School

We'd like our page to look very much like http://www.moveonpinegrove.example/. I've attached our text and you can see how I've tried to make it similar to their site in placement.
We'd like to do a darker green instead of their blue shading, obviously our logo (the dragon image) instead of theirs, our student photo or a better image you may choose, and instead of a solid block of text under "Welcome . . ." we'd like the USA Badge to the right of the text. At the bottom of the page we'd like a big button with our phone number. I know this is a lot to take in, but we're so looking forward to seeing your designs!

These designs are looking good! I'm sending each of you a few suggested tweaks for now! Best of luck!

As we enter the final few days of competition, I'd like to give a final word of thanks to all of our designers. We have moved out of good and into excellent, and we thank you all. We've also updated the student image we'd like you to use. All of the remaining designers will need to update their photos with the new one, please. Also, if you've one of the final designs, I'll be sending you a final set of notes and then we will be selecting someone. We may push back the final selection until Monday, depending.

Reason: We're going to discuss the finalized versions of your designs on Monday and make our final selection. If for some reason, none of the designers have made our suggested tweaks, then we still have another day.

```html
<!DOCTYPE html>
<html lang="en">
<head>
<meta charset="utf-8">
<title>Pinegrove TaeKwonDo</title>
<link href="https://fonts.googleapis.com/css2?family=Barlow+Semi+Condensed:wght@600&family=Open+Sans:wght@400&display=swap" rel="stylesheet">
<style>
:root{
  --green:#6a9a1f;
  --green-bright:#9ccb2e;
  --green-mid:#7db227;
  --green-dark:#4a7208;
  --tint-top:#e6f6c0;
  --tint-bottom:#d9f0b2;
  --ink:#2b2b2b;
  --nav:#3a3a3a;
  --white:#ffffff;
}
*{margin:0;padding:0;box-sizing:border-box}
html,body{width:1143px;height:1200px;overflow:hidden;background:var(--white)}
body{font-family:"Open Sans",sans-serif;color:var(--ink)}
.display{font-family:"Barlow Semi Condensed",sans-serif;font-weight:600}

.site-header{position:relative;height:128px;background:linear-gradient(#f3f3f3,#ffffff 40%,#fafafa)}
.brand{position:absolute;left:170px;top:40px;display:flex;align-items:center;gap:10px}
.brand-mark{width:44px;height:44px;border-radius:50%;border:3px solid #111}
.brand-name{font-family:"Barlow Semi Condensed",sans-serif;font-weight:600;font-size:17px;color:#111;line-height:1.1;width:110px}
.main-nav{position:absolute;left:409px;top:57px;display:flex;align-items:center}
.main-nav a{font-family:"Barlow Semi Condensed",sans-serif;font-weight:600;font-size:17px;color:var(--nav);text-decoration:none;text-transform:uppercase;letter-spacing:.3px}
.main-nav .sep{width:1px;height:12px;background:#c8c8c8;margin:0 12px}
.call-cta{position:absolute;left:820px;top:24px;width:153px;height:80px;background:linear-gradient(var(--green-bright),var(--green-mid));color:var(--white);font-family:"Barlow Semi Condensed",sans-serif;font-weight:600;font-size:16px;line-height:19px;padding:13px 0 0 14px;text-transform:uppercase}

.hero{height:421px;background:linear-gradient(100deg,#3a2c28 0%,#b9a79a 30%,#2a2424 55%,#c9b9ab 80%,#403634 100%)}

.welcome{height:259px;background:linear-gradient(var(--tint-top),var(--tint-bottom));position:relative}
.welcome h1{position:absolute;left:169px;top:25px;font-size:19px;color:var(--green);text-transform:uppercase;letter-spacing:.3px}
.welcome-copy{position:absolute;left:169px;top:58px;width:680px;font-size:11.2px;line-height:19px}
.welcome-copy p{margin-bottom:19px}
.badge{position:absolute;left:872px;top:84px;width:100px;height:100px;border-radius:50%;background:var(--white);border:4px solid #d22a2a;box-shadow:inset 0 0 0 6px #f1f1f1,inset 0 0 0 9px #2a3a9a}

.classes{height:232px;position:relative}
.class-row{position:absolute;left:172px;width:770px;display:flex}
.class-row h2{width:261px;font-size:22px;color:var(--green);line-height:1}
.class-row p{width:510px;font-size:11.2px;line-height:18px;margin-top:-5px}

.hear-from-you{height:113px;background:linear-gradient(var(--green-bright),var(--green-mid));color:var(--white);text-align:center;font-size:25px;line-height:34px;padding-top:23px;letter-spacing:.3px}
.site-footer{height:47px;background:var(--green-dark);color:var(--white);text-align:center;font-size:12px;line-height:47px}
</style>
</head>
<body>
<header class="site-header">
  <div class="brand"><span class="brand-mark"></span><span class="brand-name">Pinegrove Tae Kwon Do</span></div>
  <nav class="main-nav">
    <a href="#">Home</a><span class="sep"></span>
    <a href="#">About Us</a><span class="sep"></span>
    <a href="#">Our Classes</a><span class="sep"></span>
    <a href="#">Contact Us</a>
  </nav>
  <div class="call-cta">Call today for a<br>free lesson<br>555 014-2288</div>
</header>

<section class="hero" role="img" aria-label="Photo of young students in black uniforms practising kicks on pads in the training hall"></section>

<section class="welcome">
  <h1 class="display">Welcome to Pinegrove TaeKwonDo!</h1>
  <div class="welcome-copy">
    <p>Are you interested in Pinegrove TaeKwonDo classes, lessons, sparring, training, or one-on-one private tutoring in the martial arts? We are a full time martial arts academy based in Pinegrove, OR. We offer a range of TaeKwonDo, or Korean Karate, classes for all skill levels, but we specialize in TaeKwonDo for kids and teens!</p>
    <p>TaeKwonDo training is in a safe, friendly school under the car of an instructor with 20 years of experience in martial arts. Our Instructor, Dana Whitfield, was voted 2014’s Children’s Instructor of the Year by the National Martial Arts Honor Guild! Learn with the best!</p>
    <p>We are located at 48 W. Elm Street right in Downtown, Pinegrove, OR. One block East of Harlow’s Diner, across the street from Pinegrove Arts Hall, Two Doors Down from Copper Note Club, and directly between Marlo’s on Elm and Stillwater Yoga.</p>
  </div>
  <div class="badge" role="img" aria-label="Honor guild badge"></div>
</section>

<section class="classes">
  <div class="class-row" style="top:44px"><h2 class="display">Beginners (ages 3-7)</h2><p>It is a fun, energetic introduction to the art. Students begin to learn forms. This class accepts young students.</p></div>
  <div class="class-row" style="top:99px"><h2 class="display">Intermediate (ages 6-15)</h2><p>Children learn martial arts, respect, and self-defense in a safe environment. This class is based on experience level and accepts students with some experience in the art.</p></div>
  <div class="class-row" style="top:155px"><h2 class="display">Advanced (ages 8-14)</h2><p>For students who have some experience past the basic level. We cover more advanced topics, higher-kicks and more sparring. We prep our students for the challenges of confrontation, bullying, and self-defense.</p></div>
</section>

<section class="hear-from-you display">We’d Love to Hear From You!<br>Call 555 014-2288</section>
<footer class="site-footer">48 W Elm Street Pinegrove, OR 97099</footer>
</body>
</html>
```